Panel Fest Poster

Our school is hosting a Panel Fest event at our school, open to the public, geared toward kids with sensory needs. We need a poster to advertise the event. The event will be held on March 16, 2019 at The Birchfield School at Dunmore (417 Larkspur Lane, Horsham, PA). Registration is required:https://www.birchfieldacad.org/admissions/admissions-visit-and-events

Do you love Comics, Milo Brackett, Zintaro, and other adventure characters? Then join us here at TBS for our first ever Panel Fest! Our classrooms will transform into wonderlands of your favorite movies and comics, filled with crafts, games, and more. Be sure to dress up as your favorite characters! This event is free but registration is required.

```html
<!DOCTYPE html>
<html lang="en">
<head>
<meta charset="utf-8">
<title>Panel Fest Poster</title>
<link rel="stylesheet" href="https://fonts.googleapis.com/css2?family=Bangers&family=Luckiest+Guy&family=Poppins:wght@600&display=swap">
<style>
  :root {
    --gold: #d3b54c;
    --green: #294a31;
    --red: #ea4a2c;
    --ink: #121212;
    --paper: #ffffff;
    --burst: #ececec;
  }
  * { margin: 0; padding: 0; box-sizing: border-box; }
  html, body { width: 938px; height: 1200px; overflow: hidden; background: var(--paper); }
  .poster { position: relative; width: 938px; height: 1200px; overflow: hidden; background: var(--paper); font-family: "Bangers", cursive; }
  .burst-backdrop { position: absolute; left: 0; top: 96px; width: 938px; height: 1030px;
    background: radial-gradient(ellipse at 50% 45%, var(--paper) 35%, var(--burst) 100%); }
  .top-band { position: absolute; left: 0; top: 30px; width: 938px; height: 66px; background: var(--ink); }
  .tagline-box { position: absolute; left: 0; top: 0; width: 570px; height: 62px; background: var(--gold);
    display: flex; align-items: center; padding-left: 56px; }
  .tagline { font-family: "Luckiest Guy", cursive; font-size: 21px; color: var(--ink); letter-spacing: .5px; }
  .date-shape { position: absolute; left: 660px; top: 0; width: 278px; height: 215px; }
  .date { position: absolute; left: 700px; top: 40px; width: 230px; color: var(--gold); font-family: "Luckiest Guy", cursive; }
  .date-day { position: absolute; left: 0; top: 0; font-size: 72px; line-height: 1; color: var(--red); }
  .date-month { position: absolute; left: 92px; top: 6px; font-size: 30px; line-height: 1.05; color: var(--red); }
  .date-year { color: var(--gold); display: block; }
  .date-venue { position: absolute; left: 0; top: 84px; width: 230px; text-align: right; font-size: 18px; line-height: 1.15; }
  .date-venue small { font-size: 13px; display: block; }
  .title { position: absolute; left: 70px; top: 92px; font-family: "Luckiest Guy", cursive; color: var(--red);
    text-shadow: 4px 4px 0 #7a1d10, 8px 8px 0 var(--ink); transform: rotate(-3deg); line-height: .9; }
  .title-line-one { display: block; font-size: 150px; letter-spacing: 2px; }
  .title-line-two { display: block; font-size: 96px; margin-left: 170px; }
  .intro { position: absolute; left: 55px; top: 345px; width: 830px; text-align: center; color: var(--gold);
    font-family: "Luckiest Guy", cursive; font-size: 38px; line-height: 54px; }
  .intro em { font-style: normal; color: var(--red); }
  .details { position: absolute; left: 75px; top: 606px; width: 800px; text-align: center; color: var(--red);
    font-size: 29px; line-height: 40px; letter-spacing: .6px; transform: skewX(-6deg); }
  .reg-cloud { position: absolute; left: 0; top: 830px; width: 500px; height: 300px; }
  .registration { position: absolute; left: 18px; top: 960px; width: 460px; text-align: center; }
  .registration-head { font-family: "Luckiest Guy", cursive; font-size: 58px; color: var(--paper); line-height: 1; }
  .registration-sub { font-family: "Luckiest Guy", cursive; font-size: 34px; color: var(--gold); line-height: 1.1; }
  .registration-note { font-family: "Poppins", sans-serif; font-size: 12px; color: var(--red); margin-top: 4px; }
  .costume-box { position: absolute; left: 488px; top: 987px; width: 450px; height: 136px; background: var(--gold);
    display: flex; align-items: center; justify-content: center; text-align: center;
    font-family: "Luckiest Guy", cursive; font-size: 28px; line-height: 34px; color: var(--paper); }
  .footer-band { position: absolute; left: 0; top: 1123px; width: 938px; height: 77px; background: var(--ink);
    display: flex; align-items: center; padding-left: 26px; }
  .footer-url { font-family: "Poppins", sans-serif; font-weight: 600; font-size: 20.5px; color: var(--red); white-space: nowrap; }
</style>
</head>
<body>
<main class="poster">
  <div class="burst-backdrop" role="img" aria-label="Comic-style radiating burst lines and halftone dots behind the text"></div>

  <div class="top-band"></div>
  <div class="tagline-box"><p class="tagline">Best New Stories Every Week</p></div>

  <svg class="date-shape" viewBox="0 0 278 215" aria-hidden="true">
    <path fill="var(--green)" d="M0 0 H278 V200 Q250 222 222 200 Q200 220 170 200 Q140 220 110 200 Q80 222 55 198 Q20 205 24 170 Q0 150 20 125 Q-2 100 14 80 Z"/>
  </svg>
  <div class="date">
    <span class="date-day">16</span>
    <span class="date-month">March<span class="date-year">2019</span></span>
    <p class="date-venue"><small>The Birchfield School</small>at Dunmore</p>
  </div>

  <h1 class="title"><span class="title-line-one">Panel</span><span class="title-line-two">Fest</span></h1>

  <p class="intro">Do you love comics, Milo Brackett, Zintaro, and other adventure characters? Then join us here <em>at TBS</em> for our <em>first ever Panel Fest!</em></p>

  <p class="details">Our classrooms will transform into wonderlands of your favorite movies and comics, filled with crafts, games, and more. Be sure to dress up as your favorite characters! This event is free but registration is required.</p>

  <svg class="reg-cloud" viewBox="0 0 500 300" aria-hidden="true">
    <g fill="var(--green)">
      <circle cx="60" cy="90" r="70"/>
      <circle cx="170" cy="70" r="72"/>
      <circle cx="280" cy="95" r="68"/>
      <circle cx="390" cy="140" r="75"/>
      <circle cx="440" cy="220" r="70"/>
      <rect x="0" y="90" width="480" height="210"/>
    </g>
  </svg>
  <div class="registration">
    <p class="registration-head">Registration</p>
    <p class="registration-sub">Is Required</p>
    <p class="registration-note">This event is free but registration is required.</p>
  </div>

  <div class="costume-box"><p>Be sure to dress up<br>as your favorite<br>characters!</p></div>

  <footer class="footer-band"><p class="footer-url">https://www.birchfieldacad.org/admissions/admissions-visit-and-events</p></footer>
</main>
</body>
</html>
```